Business Card for Business consulting practice

Need a design for a consultant business card. Simple and elegant.
I need the following information on the card:
Logo: (see uploaded file)
Company name: Calmora Advisory Group
Name: Dana Weltrup
Title: Managing Director - Aerospace and Defence
Phone #: 514-268-3917
e-mail: dana.weltrup@calmora-example.com
Website: www.calmora-example.com
Tagline: Proposals Management and Capture support for complex procurements

```html
<!DOCTYPE html>
<html lang="en">
<head>
<meta charset="utf-8">
<title>Calmora Advisory Group – Business Card</title>
<link rel="stylesheet" href="https://fonts.googleapis.com/css2?family=Fira+Sans+Condensed:wght@500;600;700&display=swap">
<style>
  :root {
    --navy: #0d2440;
    --teal: #3bbfd3;
    --paper: #ffffff;
    --swoosh: #e6e6e6;
    --font: "Fira Sans Condensed", sans-serif;
  }
  html, body {
    margin: 0;
    padding: 0;
    overflow: hidden;
    background: #ffffff;
  }
  .card {
    position: relative;
    width: 1200px;
    height: 686px;
    background: var(--navy);
    font-family: var(--font);
    overflow: hidden;
  }
  .card-face {
    position: absolute;
    left: 34px;
    top: 34px;
    width: 1132px;
    height: 618px;
    background: var(--paper);
  }
  .swoosh {
    position: absolute;
    left: 0;
    top: 0;
  }
  .company-name {
    position: absolute;
    left: 0;
    width: 1200px;
    top: 140px;
    margin: 0;
    text-align: center;
    font-size: 70px;
    font-weight: 600;
    letter-spacing: 3px;
    text-transform: uppercase;
    color: var(--navy);
    line-height: 1;
  }
  .person {
    position: absolute;
    left: 110px;
    width: 400px;
    top: 330px;
    text-align: center;
  }
  .person-name {
    margin: 0;
    font-size: 55px;
    font-weight: 700;
    color: var(--teal);
    text-transform: uppercase;
    line-height: 1;
    white-space: nowrap;
  }
  .person-title {
    margin: 30px 0 0;
    font-size: 35px;
    font-weight: 600;
    color: var(--navy);
    line-height: 1.15;
  }
  .person-division {
    display: block;
    font-size: 27px;
  }
  .divider {
    position: absolute;
    left: 528px;
    top: 337px;
    width: 2px;
    height: 177px;
    background: var(--teal);
  }
  .contacts {
    position: absolute;
    left: 558px;
    top: 340px;
    margin: 0;
    padding: 0;
    list-style: none;
  }
  .contact {
    display: flex;
    align-items: center;
    height: 52px;
    margin-bottom: 16px;
    font-size: 31px;
    font-weight: 500;
    color: var(--navy);
    white-space: nowrap;
  }
  .contact-icon {
    width: 52px;
    height: 52px;
    margin-right: 16px;
    flex: none;
  }
</style>
</head>
<body>
  <main class="card">
    <div class="card-face"></div>

    <svg class="swoosh" width="1200" height="686" viewBox="0 0 1200 686" aria-hidden="true">
      <path d="M34,634 L1034,528 Q1046,514 1029,491 L1000,463 Q1086,503 1166,537 L1166,652 L34,652 Z" fill="var(--swoosh)"/>
    </svg>

    <h1 class="company-name">Calmora Advisory Group</h1>

    <section class="person">
      <h2 class="person-name">Dana Weltrup</h2>
      <p class="person-title">Managing Director<span class="person-division">- Aerospace and Defence</span></p>
    </section>

    <div class="divider"></div>

    <ul class="contacts">
      <li class="contact">
        <svg class="contact-icon" viewBox="0 0 52 52" aria-hidden="true">
          <circle cx="26" cy="26" r="26" fill="var(--teal)"/>
          <path d="M18 14 l5 0 l2 7 l-3 2 q2 5 7 8 l2 -3 l7 2 l0 5 q-1 3 -4 3 q-10 -1 -16 -8 q-5 -6 -4 -13 q0 -3 4 -3 z" fill="#ffffff"/>
          <path d="M30 16 q5 1 6 6 M30 11 q9 2 11 11" stroke="#ffffff" stroke-width="2" fill="none" stroke-linecap="round"/>
        </svg>
        514-268-3917
      </li>
      <li class="contact">
        <svg class="contact-icon" viewBox="0 0 52 52" aria-hidden="true">
          <circle cx="26" cy="26" r="26" fill="var(--teal)"/>
          <text x="26" y="34" text-anchor="middle" font-family="Fira Sans Condensed, sans-serif" font-weight="700" font-size="24" fill="#ffffff">@</text>
        </svg>
        dana.weltrup@calmora-example.com
      </li>
      <li class="contact">
        <svg class="contact-icon" viewBox="0 0 52 52" aria-hidden="true">
          <circle cx="26" cy="26" r="26" fill="var(--teal)"/>
          <g fill="none" stroke="#ffffff" stroke-width="2">
            <circle cx="26" cy="26" r="13"/>
            <ellipse cx="26" cy="26" rx="6" ry="13"/>
            <line x1="13" y1="26" x2="39" y2="26"/>
            <line x1="26" y1="13" x2="26" y2="39"/>
            <path d="M15 19 h22 M15 33 h22"/>
          </g>
        </svg>
        www.calmora-example.com
      </li>
    </ul>
  </main>
</body>
</html>
```